Maple Vita App Landing Page

Looking for a landing page for our app at maplevitaco.example

Target Market(s)

Health care facilities

Industry/Entity Type

Healthcare

Number of Pages Required

1 page

```html
<!DOCTYPE html>
<html lang="en">
<head>
<meta charset="utf-8">
<title>Maple Vita – COVID-19 Screening App</title>
<link rel="stylesheet" href="https://fonts.googleapis.com/css2?family=Poppins:wght@300;400;500;600&family=Courier+Prime&display=swap">
<style>
:root{
  --blue:#3d7ff0;
  --violet:#b066ef;
  --ink:#1d2233;
  --body:#4c5366;
  --muted:#8a90a2;
  --pale:#f4f6fc;
  --row:#f3f5fa;
  --teal:#1c8f9a;
  --coral:#f35b3f;
  --cyan:#12cfe0;
  --black:#111;
  --white:#fff;
}
*{box-sizing:border-box;margin:0;padding:0}
html,body{width:1200px;height:4448px;overflow:hidden}
body{position:relative;font-family:"Poppins",sans-serif;color:var(--ink);background:var(--white)}
.abs{position:absolute}
.grad{background:linear-gradient(90deg,var(--blue),var(--violet))}
.brand{display:flex;align-items:center;gap:12px;color:var(--white)}
.brand-dot{width:40px;height:40px;border-radius:50%;background:var(--white);opacity:.9}
.brand-name{font-size:28px;font-weight:600;letter-spacing:.5px}
.brand-tag{font-size:12px;color:var(--white);opacity:.9}
.store{display:flex;align-items:center;gap:10px;background:var(--black);color:var(--white);border-radius:26px;height:46px;padding:0 18px;font-size:17px;font-weight:500}
.store i{width:20px;height:20px;border-radius:50%;background:var(--white);display:block}
.store small{display:block;font-size:7px;letter-spacing:.5px;line-height:1}
.label{font-size:11px;font-weight:500;color:var(--blue);letter-spacing:.5px;text-transform:uppercase}
.h2{font-size:28px;font-weight:500;color:var(--ink)}
.para{font-size:12px;line-height:22px;color:var(--body)}
.btn{display:flex;align-items:center;justify-content:center;color:var(--white);font-size:11px;font-weight:500;border-radius:26px;box-shadow:0 8px 18px rgba(61,127,240,.3);text-transform:uppercase}
.phone{background:var(--white);border-radius:30px;box-shadow:0 14px 40px rgba(40,50,90,.18);padding:12px}
.screen{border:1px solid #e5e7ee;border-radius:18px;overflow:hidden;height:100%;background:var(--white);position:relative}
.bar{color:var(--white);text-align:center;font-size:10px;font-weight:500;padding:12px 6px 8px;line-height:1.2}
.bar small{display:block;font-size:5px;opacity:.8}
.field{border:1px solid var(--coral);border-radius:3px;height:22px;font-size:7px;color:var(--muted);padding:5px 6px;margin:0 10px}
.go{color:var(--white);font-size:7px;border-radius:3px;height:18px;padding:4px 8px;margin:0 10px;display:flex;justify-content:space-between}
.mono{font-family:"Courier Prime",monospace;font-size:8.5px;line-height:10px;color:var(--ink);padding:0 14px}
.art{border-radius:8px;background:linear-gradient(160deg,#dfe8ff,#9fb4ff 60%,#3d59e8)}
.card{background:var(--white);border-radius:10px;box-shadow:0 10px 30px rgba(40,50,90,.08);padding:20px}
.card .ico{width:60px;height:60px;border-radius:10px;margin-bottom:28px}
.card h4{font-size:15px;font-weight:500;margin-bottom:14px}
.card p{font-size:11px;line-height:19px;color:var(--muted)}
.plan{background:var(--white);text-align:center}
.plan h4{font-size:19px;font-weight:400;margin:46px 0 24px}
.plan ul{list-style:none;width:220px;margin:0 auto}
.plan li{font-size:12px;color:var(--body);height:40px;line-height:40px}
.plan li:nth-child(odd){background:var(--row)}
.price{font-size:42px;color:var(--blue);font-weight:400;margin:22px 0 8px}
.price sup{font-size:22px;vertical-align:18px}
.price span{font-size:16px;color:var(--body)}
.social{display:flex;gap:14px}
.social i{width:12px;height:12px;border-radius:50%;background:var(--white);display:block}
</style>
</head>
<body>

<!-- hero -->
<svg class="abs" style="left:0;top:0" width="1200" height="560" viewBox="0 0 1200 560" aria-hidden="true">
  <defs><linearGradient id="hg" x1="0" x2="1"><stop offset="0" stop-color="#3d7ff0"/><stop offset="1" stop-color="#c069ef"/></linearGradient></defs>
  <path d="M0 0H1200V280C1080 300 1020 400 900 470C780 540 620 560 500 500C380 440 300 360 170 370C90 376 40 400 0 420Z" fill="url(#hg)"/>
</svg>
<div class="abs" style="left:155px;top:24px">
  <div class="brand"><i class="brand-dot"></i><span class="brand-name">MAPLE VITA</span></div>
  <div class="brand-tag" style="margin:2px 0 0 125px">Keeping you safe</div>
</div>
<h1 class="abs" style="left:154px;top:135px;font-size:37px;line-height:40px;font-weight:500;color:var(--white)">COVID-19<br>Screening App</h1>
<p class="abs" style="left:154px;top:238px;font-size:18px;line-height:26px;color:var(--white);font-weight:300">Maple Vita Provide COVID-19 Screening App<br>whhich will keep you safe</p>
<div class="abs store" style="left:154px;top:352px;width:153px"><i></i><div><small>GET IT ON</small>PlayHub</div></div>
<div class="abs store" style="left:322px;top:352px;width:153px"><i></i><div><small>DOWNLOAD ON THE</small>AppHub</div></div>

<div class="abs phone" style="left:783px;top:85px;width:235px;height:480px">
  <div class="screen">
    <div class="bar grad" style="padding-top:30px;margin:0 10px">COVID-19 SCREENING<small>SCREENING • WELCOME</small></div>
    <div style="display:flex;justify-content:center;align-items:center;gap:6px;margin-top:30px;color:var(--blue);font-weight:600;font-size:17px"><i style="width:14px;height:14px;border-radius:50%;background:var(--blue)"></i>MAPLE VITA</div>
    <div style="text-align:center;font-size:7px;color:var(--blue)">Keeping you safe</div>
    <div class="art" role="img" aria-label="Illustration of people waiting at a distance" style="margin:22px 30px 0;height:150px"></div>
    <div class="go" style="background:var(--blue);margin:40px 15px 0;height:24px;padding:7px 10px">Start your COVID-19 screening now<span>›</span></div>
  </div>
</div>

<!-- features -->
<svg class="abs" style="left:720px;top:645px" width="420" height="420" aria-hidden="true"><defs><linearGradient id="cg" x1="0" y1="0" x2="0" y2="1"><stop offset="0" stop-color="#a36df0"/><stop offset="1" stop-color="#3f6cf0"/></linearGradient></defs><circle cx="210" cy="210" r="205" fill="url(#cg)"/></svg>
<div class="abs label" style="left:154px;top:789px">Checkout Features</div>
<h2 class="abs" style="left:154px;top:812px;font-size:29px;line-height:30px;font-weight:500">The only app<br>you will need</h2>
<svg class="abs" style="left:155px;top:896px" width="70" height="20" aria-hidden="true"><path d="M2 10H22M2 10L8 5M2 10L8 15" stroke="#3d7ff0" stroke-width="2" fill="none"/><path d="M44 10H64M64 10L58 5M64 10L58 15" stroke="#3d7ff0" stroke-width="2" fill="none"/></svg>
<div class="abs card" style="left:440px;top:730px;width:275px;height:225px"><div class="ico" style="background:linear-gradient(135deg,#7be8e0,#3ac6d8)"></div><h4>Lorem Ipsum Dolor Sit</h4><p>Direct mailing research development buyer tablet validation startup social proof learning curve user experience analytics</p></div>
<div class="abs card" style="left:743px;top:730px;width:275px;height:225px"><div class="ico" style="background:linear-gradient(135deg,#ffe08a,#ffbf3a)"></div><h4>Lorem Ipsum Dolor Sit</h4><p>Direct mailing research development buyer tablet validation startup social proof learning curve user experience analytics</p></div>
<div class="abs card" style="left:1046px;top:730px;width:275px;height:225px"><div class="ico" style="background:linear-gradient(135deg,#c9b6ff,#8c8cf5)"></div><h4>Lorem Ipsum Dolor Sit</h4><p>Direct mailing research development buyer tablet validation startup social proof learning curve user experience analytics</p></div>

<!-- section: admin -->
<div class="abs" style="left:0;top:1100px;width:1200px;height:490px;background:var(--pale)"></div>
<div class="abs phone" style="left:255px;top:1150px;width:195px;height:400px">
  <div class="screen">
    <div class="bar" style="background:var(--teal);padding-top:20px">COVID-19 ADMIN SCREEN<small>ADMIN SCREEN • VENDOR EXCEPTION</small></div>
    <div class="mono" style="text-align:center;color:var(--teal);font-weight:700;margin:12px 0 8px">Vendor Exception</div>
    <div class="mono">In an effort to minimize exposure risk to all of our residents, we are restricting vendors from entering the facility. Thank you for completing this screening process.<br><br>I, Name/Title ______, am employed by ______ and request an essential visit for the following reason(s): ______ I am attesting that my visit is necessary and imminent in nature.</div>
    <div style="font-size:6px;color:var(--muted);margin:10px 14px 0;border-bottom:1px solid #ccc;padding-bottom:2px">Entity Phone Number</div>
    <div style="font-size:6px;color:var(--muted);margin:10px 14px 0;border-bottom:1px solid #ccc;padding-bottom:2px">Entity email</div>
  </div>
</div>
<div class="abs" style="left:420px;top:1178px;width:96px;height:96px;border-radius:50%;background:linear-gradient(135deg,#9d8ff5,#5d7df2);box-shadow:0 10px 24px rgba(80,100,240,.35)"></div>
<div class="abs label" style="left:580px;top:1228px">01 - Checkout Features</div>
<h2 class="abs h2" style="left:580px;top:1252px">Lorem ipsum dolor sit amets</h2>
<p class="abs para" style="left:580px;top:1301px;width:440px">There are many variations of passages of lorem ipsum available, but the majority have suffered alteration in some form, by injected humour lorem ipsum is simply free text in the</p>
<div class="abs btn grad" style="left:586px;top:1400px;width:157px;height:48px">Get Started Now</div>

<!-- section: triage -->
<svg class="abs" style="left:0;top:1590px" width="1200" height="660" aria-hidden="true"><path d="M0 0H1200V560C1050 600 900 520 720 540C520 560 300 600 120 620C70 626 30 636 0 650Z" fill="#f4f6fc"/></svg>
<div class="abs label" style="left:212px;top:1800px">01 - Checkout Features</div>
<h2 class="abs h2" style="left:212px;top:1824px">Lorem ipsum dolor sit amets</h2>
<p class="abs para" style="left:212px;top:1873px;width:440px">There are many variations of passages of lorem ipsum available, but the majority have suffered alteration in some form, by injected humour lorem ipsum is simply free text in the</p>
<div class="abs btn grad" style="left:218px;top:1972px;width:157px;height:48px">Get Started Now</div>
<div class="abs phone" style="left:755px;top:1712px;width:198px;height:400px">
  <div class="screen">
    <div class="bar" style="background:var(--coral);padding-top:16px">COVID-19 TRIAGE<small>TRIAGE • TEMPERATURE</small></div>
    <div style="text-align:center;font-size:7px;color:var(--coral);margin:12px 16px 14px">Please go to reception desk for a temperature reading</div>
    <div style="text-align:center;font-size:7px;color:var(--coral);margin-bottom:6px">Temperature</div>
    <div class="field">98.6°F</div>
    <div style="text-align:center;font-size:7px;color:var(--coral);margin:24px 0 6px">Nurse ID</div>
    <div class="field">####</div>
    <div class="go" style="background:var(--coral);margin-top:12px">Next<span>›</span></div>
  </div>
</div>
<div class="abs" style="left:928px;top:1738px;width:98px;height:98px;border-radius:50%;background:var(--cyan);box-shadow:0 10px 24px rgba(18,207,224,.35)"></div>

<!-- screens -->
<div class="abs label" style="left:0;width:1200px;text-align:center;top:2242px">App Screen</div>
<h2 class="abs h2" style="left:0;width:1200px;text-align:center;top:2265px">How Our App Looks Like</h2>
<div class="abs" style="left:85px;top:2342px;width:155px;height:395px;background:var(--white);box-shadow:0 6px 18px rgba(40,50,90,.1);opacity:.35;overflow:hidden">
  <div class="bar" style="background:var(--teal);margin-left:-65px">COVID-19 ADMIN SCREEN<small>ADMIN SCREEN • VENDOR</small></div>
  <div class="mono" style="margin-top:14px">Vendor Exception<br><br>effort to minimize risk to all of residents, we are restricting vendors from entering the facility.</div>
</div>
<div class="abs" style="left:253px;top:2342px;width:220px;height:395px;background:var(--white);box-shadow:0 6px 18px rgba(40,50,90,.1)">
  <div class="bar" style="background:var(--blue)">COVID-19 SCREENING<small>SCREENING • WELCOME</small></div>
  <div style="display:flex;justify-content:center;align-items:center;gap:6px;margin-top:28px;color:var(--blue);font-weight:600;font-size:16px"><i style="width:13px;height:13px;border-radius:50%;background:var(--blue)"></i>MAPLE VITA</div>
  <div style="text-align:center;font-size:7px;color:var(--blue)">Keeping you safe</div>
  <div class="art" role="img" aria-label="Illustration of people waiting at a distance" style="margin:20px 28px 0;height:140px"></div>
  <div class="go" style="background:var(--blue);margin:40px 20px 0;height:22px;padding:6px 10px">Start your COVID-19 screening now<span>›</span></div>
</div>
<div class="abs" style="left:489px;top:2342px;width:220px;height:395px;background:var(--white);box-shadow:0 6px 18px rgba(40,50,90,.1)">
  <div class="bar" style="background:var(--blue)">COVID-19 SCREENING<small>SCREENING • STEP 1</small></div>
  <div style="text-align:center;font-size:8px;color:var(--blue);margin:30px 0 8px">Who are you?</div>
  <div style="display:grid;grid-template-columns:1fr 1fr;gap:8px;margin:0 16px">
    <div style="border:1px solid var(--blue);height:48px;border-radius:3px;font-size:6px;color:var(--blue);text-align:center;padding-top:34px">STAFF</div>
    <div style="border:1px solid var(--blue);height:48px;border-radius:3px;font-size:6px;color:var(--blue);text-align:center;padding-top:34px">PROVIDER</div>
    <div style="background:var(--blue);height:48px;border-radius:3px;font-size:6px;color:var(--white);text-align:center;padding-top:34px">VISITOR</div>
    <div style="border:1px solid var(--blue);height:48px;border-radius:3px;font-size:6px;color:var(--blue);text-align:center;padding-top:34px">VENDOR</div>
  </div>
  <div style="text-align:center;font-size:7px;color:var(--blue);margin:14px 0 8px">Which facility are you at?</div>
  <div class="field" style="border-color:var(--blue);margin:0 16px;color:var(--ink)">Riverside Campus</div>
  <div class="go" style="background:var(--blue);margin:12px 16px 0">Next<span>›</span></div>
</div>
<div class="abs" style="left:720px;top:2342px;width:220px;height:395px;background:var(--white);box-shadow:0 6px 18px rgba(40,50,90,.1)">
  <div class="bar" style="background:var(--coral)">COVID-19 TRIAGE<small>TRIAGE • TEMPERATURE</small></div>
  <div style="text-align:center;font-size:8px;color:var(--coral);margin:16px 30px 20px">Please go to reception desk for a temperature reading</div>
  <div style="text-align:center;font-size:8px;color:var(--coral);margin-bottom:8px">Temperature</div>
  <div class="field" style="margin:0 16px">98.6°F</div>
  <div style="text-align:center;font-size:8px;color:var(--coral);margin:26px 0 8px">Nurse ID</div>
  <div class="field" style="margin:0 16px">####</div>
  <div class="go" style="background:var(--coral);margin:14px 16px 0">Next<span>›</span></div>
</div>
<div class="abs" style="left:965px;top:2342px;width:115px;height:395px;background:var(--white);box-shadow:0 6px 18px rgba(40,50,90,.1);opacity:.45;overflow:hidden">
  <div class="bar" style="background:var(--teal);width:220px;text-align:left;padding-left:26px">COVID-19 ADMIN<small>ADMIN SCREEN</small></div>
  <div class="mono" style="margin-top:14px;width:220px;padding-left:32px">Vendor Exception<br>In an effort to minimize exposure risk to all our residents, we are restricting vendors</div>
</div>
<svg class="abs" style="left:545px;top:2832px" width="110" height="16" aria-hidden="true"><circle cx="8" cy="8" r="6" fill="#3d7ff0"/><circle cx="26" cy="8" r="6" fill="#2a2f45"/><circle cx="44" cy="8" r="6" fill="#2a2f45"/><circle cx="62" cy="8" r="6" fill="#2a2f45"/><circle cx="80" cy="8" r="6" fill="#2a2f45"/><circle cx="98" cy="8" r="6" fill="#2a2f45"/></svg>

<!-- pricing -->
<div class="abs label" style="left:0;width:1200px;text-align:center;top:2940px">Pricing</div>
<h2 class="abs h2" style="left:0;width:1200px;text-align:center;top:2964px">Built For Covid-19 Screeining</h2>
<div class="abs plan" style="left:175px;top:3052px;width:245px">
  <h4>Startup Plan</h4><ul><li>10 pages</li><li>500 gb storage</li><li>10 sdd Database</li><li>Free coustom domain</li><li>24/7 free support</li></ul>
  <div class="price"><sup>$</sup>25<span>/m</span></div>
  <div class="btn grad" style="width:157px;height:46px;margin:0 auto">Start Free Trial</div>
</div>
<div class="abs plan" style="left:449px;top:3052px;width:303px;height:493px;box-shadow:0 12px 36px rgba(40,50,90,.1)">
  <div style="background:#6b83ef;color:var(--white);font-size:10px;letter-spacing:1px;height:26px;line-height:26px">BEST PICKS</div>
  <h4 style="margin-top:20px">Startup Plan</h4><ul><li>10 pages</li><li>500 gb storage</li><li>10 sdd Database</li><li>Free coustom domain</li><li>24/7 free support</li></ul>
  <div class="price"><sup>$</sup>35<span>/m</span></div>
  <div class="btn grad" style="width:157px;height:46px;margin:0 auto">Start Free Trial</div>
</div>
<div class="abs plan" style="left:780px;top:3052px;width:245px">
  <h4>Startup Plan</h4><ul><li>10 pages</li><li>500 gb storage</li><li>10 sdd Database</li><li>Free coustom domain</li><li>24/7 free support</li></ul>
  <div class="price"><sup>$</sup>45<span>/m</span></div>
  <div class="btn grad" style="width:157px;height:46px;margin:0 auto">Start Free Trial</div>
</div>

<!-- newsletter -->
<div class="abs" style="left:0;top:3640px;width:1200px;height:250px;background:var(--pale)"></div>
<div class="abs label" style="left:0;width:1200px;text-align:center;top:3684px">Newsletter</div>
<h2 class="abs" style="left:0;width:1200px;text-align:center;top:3706px;font-size:24px;font-weight:500">Subscribe Our Newsletter</h2>
<div class="abs" style="left:323px;top:3790px;width:535px;height:48px;border-radius:26px;background:var(--white)"></div>
<div class="abs btn grad" style="left:702px;top:3790px;width:156px;height:48px;text-transform:uppercase;font-size:10px">Subscribe Now</div>

<!-- download -->
<h2 class="abs" style="left:0;width:1200px;text-align:center;top:3930px;font-size:44px;font-weight:400">Download Today</h2>
<p class="abs" style="left:0;width:1200px;text-align:center;top:4008px;font-size:17px;color:var(--body)">and get started with a free 1 month trial for your business</p>
<div class="abs store" style="left:430px;top:4082px;width:160px;height:48px"><i></i><div><small>DOWNLOAD ON THE</small>AppHub</div></div>
<div class="abs store" style="left:605px;top:4082px;width:160px;height:48px"><i></i><div><small>GET IT ON</small>PlayHub</div></div>

<!-- footer -->
<svg class="abs" style="left:0;top:4140px" width="1200" height="308" viewBox="0 0 1200 308" aria-hidden="true">
  <defs><linearGradient id="fg" x1="0" x2="1"><stop offset="0" stop-color="#c069ef"/><stop offset="1" stop-color="#3d7ff0"/></linearGradient></defs>
  <path d="M0 60C60 20 110 20 160 50C220 90 280 30 340 30C400 30 440 70 520 60C600 50 640 10 720 30C800 50 850 70 930 40C1010 10 1080 10 1130 40C1160 58 1180 60 1200 50V308H0Z" fill="url(#fg)"/>
</svg>
<div class="abs" style="left:185px;top:4250px">
  <div class="brand" style="gap:10px"><i class="brand-dot" style="width:34px;height:34px"></i><span class="brand-name" style="font-size:20px">MAPLE VITA</span></div>
  <div class="brand-tag" style="margin:0 0 0 85px;font-size:10px">Keeping you safe</div>
</div>
<div class="abs social" style="left:895px;top:4269px"><i></i><i></i><i></i><i></i><i></i><i></i></div>
<div class="abs" style="left:0;top:4388px;width:1200px;height:1px;background:rgba(255,255,255,.3)"></div>
<div class="abs" style="left:0;width:1200px;text-align:center;top:4414px;font-size:10px;color:var(--white)">© 2020 Copyrights Maple Vita</div>

</body>
</html>
```